Company Business Card

I need a Business card designed for my granite company(We install and supply Granite Counter tops). It just needs to have the employee name, title, Store address, email, and phone number. With a nifty logo design and preferably our Maplio map location on the backside. I am not creative so you can go crazy or simple on the logo.
Company Name : The Stone Harbor
Employee Name: Martin Cole
Title: Owner
Address: 4832 Fenwick Oaks Blvd. Dallas, Texas 75391
Email: Martin.Cole@SHBexample.com
Phone: 214-555-0183

```html
<!DOCTYPE html>
<html lang="en">
<head>
<meta charset="utf-8">
<title>The Stone Harbor — Business Card</title>
<link rel="stylesheet" href="https://fonts.googleapis.com/css2?family=Quicksand:wght@300;400;700&display=swap">
<style>
  :root {
    --bg: #e9e6e2;
    --card: #ffffff;
    --card-back-top: #f4f5f7;
    --card-back-bottom: #dcdee2;
    --ink: #2b2b2b;
    --ink-soft: #5a5a5a;
    --ink-muted: #a4a4a4;
    --map-light: #ece6d8;
    --map-mid: #ddd5c2;
    --brand: #7f9a92;
  }
  * { box-sizing: border-box; margin: 0; padding: 0; }
  html, body {
    width: 1200px; height: 723px; overflow: hidden;
    background: var(--bg);
    font-family: "Quicksand", sans-serif;
  }
  .stage {
    position: relative; width: 1200px; height: 723px;
    display: flex; justify-content: center; align-items: center; gap: 70px;
  }
  .card {
    position: relative; width: 330px; height: 577px;
    border-radius: 4px; overflow: hidden;
    box-shadow: 0 10px 30px rgba(0,0,0,.18);
  }
  .card--front { background: var(--card); }
  .card__map {
    position: absolute; left: -260px; top: -560px;
    width: 850px; height: 850px; border-radius: 50%;
    background: radial-gradient(circle at 55% 80%, var(--map-light), var(--map-mid));
    box-shadow: 0 4px 8px rgba(0,0,0,.22);
  }
  .card__identity { position: absolute; top: 318px; left: 0; right: 0; text-align: center; }
  .card__name { font-size: 36px; font-weight: 300; color: var(--ink); letter-spacing: .5px; }
  .card__name strong { font-weight: 700; }
  .card__title { font-size: 13px; font-weight: 400; color: var(--ink-muted); margin-top: 2px; }
  .card__contacts {
    position: absolute; top: 400px; left: 0; right: 0;
    display: flex; flex-direction: column; align-items: center; gap: 6px;
    font-size: 14px; color: var(--ink-soft);
  }
  .contact { display: flex; flex-direction: column; align-items: center; gap: 5px; }
  .contact svg { width: 18px; height: 16px; stroke: var(--ink-soft); fill: none; stroke-width: 1.4; }
  .card--back {
    background: linear-gradient(160deg, var(--card-back-top) 0%, #ffffff 35%, var(--card-back-bottom) 100%);
  }
  .brand {
    position: absolute; top: 250px; left: 0; right: 0;
    display: flex; justify-content: center; align-items: center; gap: 10px;
  }
  .brand__mark { width: 14px; height: 14px; background: var(--brand); }
  .brand__name { font-size: 26px; font-weight: 400; color: var(--brand); letter-spacing: 1px; }
</style>
</head>
<body>
<main class="stage">
  <section class="card card--front">
    <div class="card__map" role="img" aria-label="Street map showing the store location on Fenwick Oaks Blvd, Dallas"></div>
    <div class="card__identity">
      <h1 class="card__name">Martin <strong>Cole</strong></h1>
      <p class="card__title">Owner of The Stone Harbor</p>
    </div>
    <address class="card__contacts">
      <div class="contact">
        <svg viewBox="0 0 18 16" aria-hidden="true"><path d="M1 3l5-2 6 2 5-2v12l-5 2-6-2-5 2z M6 1v12 M12 3v12"/></svg>
        <span>4832 Fenwick Oaks Blvd. Dallas, Texas 75391</span>
      </div>
      <div class="contact">
        <svg viewBox="0 0 18 16" aria-hidden="true"><path d="M5 1l2 4-2 1.5c1 2.5 2.5 4 5 5L11.5 9.5l4 2-1.5 3C8 14 3 9 2.5 2.5z"/></svg>
        <span>214-555-0183</span>
      </div>
      <div class="contact">
        <svg viewBox="0 0 18 16" aria-hidden="true"><path d="M1.5 3h15v10h-15z M1.5 3l7.5 6 7.5-6"/></svg>
        <span>Martin.Cole@SHBexample.com</span>
      </div>
    </address>
  </section>

  <section class="card card--back">
    <div class="brand">
      <span class="brand__mark" aria-hidden="true"></span>
      <span class="brand__name">The Stone Harbor</span>
    </div>
  </section>
</main>
</body>
</html>
```